Bref créative |
Harbourlea Dental Clinic | ||
business cards, letterhead and envelopes design | ||
Use same font as used in my logo | ||
Cutting-Edge Corporate Traditional Modern Professional Simple Bright & Fun-filled |
Dr. Kelsi Tomberg Ravinder | ||
Corrow Arcade - Shop 4.3C, 27 Fenwick Lane, Meadowbank, NSW 2114 |
kelsi@HarbourleaDentalClinic.com.au | ||
www.HarbourleaDentalClinic.com.au | ||
For Business Cards Please include: After-hours Emergency Service: Phone: 02 5173 6648 Mobile: 04 7825 1943 For Envelops Please include: Logo If not delivered please return to Corrow Arcade - Shop 4.3C, 27 Fenwick Lane, Meadowbank, NSW 2114 |
Appointment: For - Date - Time - If you are unable to keep your appointment, please contact us as soon as possible. |

```html
<!DOCTYPE html>
<html lang="en">
<head>
<meta charset="utf-8">
<title>Harbourlea Dental Clinic – Stationery</title>
<link href="https://fonts.googleapis.com/css2?family=Raleway:wght@400;600;700;800&display=swap" rel="stylesheet">
<style>
:root{
  --bg:#ecebe8;
  --paper:#ffffff;
  --blue:#1b8fcb;
  --blue-dark:#0f6fa8;
  --blue-light:#7cc7ec;
  --ink:#3f4447;
  --grey:#8a8f93;
  --line:#c9ccce;
  --black:#1d1f21;
}
*{box-sizing:border-box;margin:0;padding:0}
html,body{width:1200px;height:430px;overflow:hidden}
body{background:var(--bg);font-family:"Raleway",Arial,sans-serif;color:var(--ink);position:relative}
.sheet{position:absolute;background:var(--paper);box-shadow:0 2px 6px rgba(0,0,0,.18);overflow:hidden}
.wave{position:absolute;left:0;bottom:0;width:100%}
.brand{display:flex;align-items:center;gap:4px}
.brand-dot{width:9px;height:9px;border-radius:50%;background:var(--blue);flex:none}
.brand-name{font-weight:700;color:var(--blue);text-transform:uppercase;letter-spacing:.3px;white-space:nowrap}
.tiny{font-size:4px;color:var(--grey);line-height:1.5;white-space:nowrap}

/* business cards */
.card-front{left:24px;top:36px;width:120px;height:54px}
.card-front .brand{position:absolute;left:6px;top:7px}
.card-front .brand-dot{width:7px;height:7px}
.card-front .brand-name{font-size:4.6px}
.card-front .person{position:absolute;right:6px;top:19px;text-align:right;font-size:4px;font-weight:700;color:var(--ink);white-space:nowrap}
.card-front .contact{position:absolute;left:7px;top:25px}
.card-back{left:149px;top:36px;width:120px;height:54px;border-radius:4px;
  background:linear-gradient(135deg,var(--blue-light),var(--blue) 55%,var(--blue-dark))}
.card-back .brand{position:absolute;left:10px;top:18px}
.card-back .brand-dot{background:#fff}
.card-back .brand-name{color:#fff;font-size:6px}
.card-back .tiny{position:absolute;left:10px;top:32px;color:#e5f4fc}

/* envelopes */
.env-front{left:19px;top:100px;width:250px;height:109px}
.env-front .brand{position:absolute;left:10px;top:12px}
.env-front .brand-name{font-size:7px}
.env-front .return{position:absolute;left:12px;top:34px}
.env-front .web{position:absolute;right:12px;bottom:8px;font-size:4.4px;color:#fff;font-weight:600}
.env-back{left:19px;top:220px;width:250px;height:111px}

/* letterhead */
.letterhead{left:288px;top:24px;width:209px;height:314px}
.letterhead .brand{position:absolute;left:14px;top:14px}
.letterhead .brand-name{font-size:6.4px}
.letterhead .web{position:absolute;left:0;right:0;bottom:6px;text-align:center;font-size:4.4px;color:#fff;font-weight:600}

/* fax */
.fax{left:516px;top:24px;width:216px;height:372px}
.fax .brand{position:absolute;left:14px;top:14px}
.fax .brand-dot{background:var(--ink)}
.fax .brand-name{font-size:7px;color:var(--ink)}
.fax-title{position:absolute;left:14px;top:40px;font-size:27px;font-weight:800;color:var(--black);letter-spacing:1px}
.fax-table{position:absolute;left:14px;top:76px;width:188px;border-collapse:collapse;font-size:4.6px}
.fax-table td{border:.6px solid #777;height:11.5px;padding:0 3px;vertical-align:middle}
.fax-table .label{width:30px;font-weight:600}
.fax-note{position:absolute;left:14px;top:152px;width:188px;height:90px;border:.6px solid #777}
.fax-checks{position:absolute;left:14px;top:250px;display:flex;gap:7px;font-size:4.2px}
.fax-checks span{display:flex;align-items:center;gap:2px;white-space:nowrap}
.fax-checks i{width:5px;height:5px;border:.6px solid #555;display:inline-block}
.fax .footer{position:absolute;left:14px;bottom:7px;font-size:3.8px;color:#fff}

/* email */
.email-label{position:absolute;left:1056px;top:32px;font-size:7px;font-weight:600;letter-spacing:.5px;color:var(--ink)}
.email-sig{left:984px;top:60px;width:209px;height:79px}
.email-sig .brand{position:absolute;left:10px;top:14px}
.email-sig .brand-dot{width:8px;height:8px}
.email-sig .brand-name{font-size:5.4px}
.email-sig .person{position:absolute;left:122px;top:12px;font-size:5px;font-weight:700;color:var(--ink);white-space:nowrap}
.email-sig .contact{position:absolute;left:122px;top:22px}
.email-card{left:989px;top:168px;width:127px;height:60px}
.email-card .brand{position:absolute;left:7px;top:8px}
.email-card .brand-name{font-size:5px}
.email-card .contact{position:absolute;left:8px;top:24px}
</style>
</head>
<body>

<div class="sheet card-front">
  <div class="brand"><span class="brand-dot"></span><span class="brand-name">Harbourlea Dental Clinic</span></div>
  <div class="person">Dr. Kelsi Tomberg Ravinder</div>
  <div class="contact tiny">Phone: 02 5173 6648<br>Mobile: 04 7825 1943<br>kelsi@HarbourleaDentalClinic.com.au</div>
  <svg class="wave" viewBox="0 0 120 14" height="14" preserveAspectRatio="none"><path d="M0 8 C40 0 80 14 120 4 V14 H0Z" fill="var(--blue)"/></svg>
</div>

<div class="sheet card-back">
  <div class="brand"><span class="brand-dot"></span><span class="brand-name">Harbourlea Dental Clinic</span></div>
  <div class="tiny">After-hours Emergency Service</div>
</div>

<div class="sheet env-front">
  <div class="brand"><span class="brand-dot"></span><span class="brand-name">Harbourlea Dental Clinic</span></div>
  <div class="return tiny">If not delivered please return to<br>Corrow Arcade - Shop 4.3C, 27 Fenwick Lane, Meadowbank, NSW 2114</div>
  <svg class="wave" viewBox="0 0 250 26" height="26" preserveAspectRatio="none">
    <path d="M0 10 C80 0 170 22 250 6 V26 H0Z" fill="var(--blue-light)"/>
    <path d="M0 16 C90 6 170 26 250 12 V26 H0Z" fill="var(--blue)"/>
  </svg>
  <div class="web">www.HarbourleaDentalClinic.com.au</div>
</div>

<div class="sheet env-back">
  <svg width="250" height="111" viewBox="0 0 250 111">
    <defs><linearGradient id="flap" x1="0" y1="0" x2="0" y2="1">
      <stop offset="0" stop-color="var(--blue-light)"/><stop offset="1" stop-color="var(--blue-dark)"/></linearGradient></defs>
    <path d="M0 0 H250 V14 C190 30 150 58 125 62 C100 58 60 30 0 14Z" fill="url(#flap)"/>
    <path d="M0 111 L110 62 M250 111 L140 62" stroke="var(--line)" stroke-width=".8" fill="none"/>
  </svg>
</div>

<div class="sheet letterhead">
  <div class="brand"><span class="brand-dot"></span><span class="brand-name">Harbourlea Dental Clinic</span></div>
  <svg class="wave" viewBox="0 0 209 26" height="26" preserveAspectRatio="none">
    <path d="M0 8 C70 0 140 20 209 4 V26 H0Z" fill="var(--blue-light)"/>
    <path d="M0 14 C70 6 140 24 209 10 V26 H0Z" fill="var(--blue)"/>
  </svg>
  <div class="web">www.HarbourleaDentalClinic.com.au</div>
</div>

<div class="sheet fax">
  <div class="brand"><span class="brand-dot"></span><span class="brand-name">Harbourlea Dental Clinic</span></div>
  <div class="fax-title">FAX</div>
  <table class="fax-table">
    <tr><td class="label">To:</td><td></td><td class="label">From:</td><td></td></tr>
    <tr><td class="label">Company:</td><td></td><td class="label">Date:</td><td></td></tr>
    <tr><td class="label">Fax:</td><td></td><td class="label">Pages:</td><td></td></tr>
    <tr><td class="label">Phone:</td><td></td><td class="label">Sender's:</td><td></td></tr>
    <tr><td class="label">Re:</td><td></td><td class="label">CC:</td><td></td></tr>
  </table>
  <div class="fax-note"></div>
  <div class="fax-checks">
    <span><i></i>Urgent</span><span><i></i>For Review</span><span><i></i>Please Comment</span><span><i></i>Please Reply</span><span><i></i>Please Recycle</span>
  </div>
  <svg class="wave" viewBox="0 0 216 24" height="24" preserveAspectRatio="none">
    <path d="M0 8 C70 0 150 18 216 4 V24 H0Z" fill="var(--grey)"/>
    <path d="M0 13 C70 6 150 22 216 10 V24 H0Z" fill="var(--black)"/>
  </svg>
  <div class="footer">Phone: 02 5173 6648 · www.HarbourleaDentalClinic.com.au</div>
</div>

<div class="email-label">E-MAIL TEMPLATE</div>
<div class="sheet email-sig">
  <div class="brand"><span class="brand-dot"></span><span class="brand-name">Harbourlea Dental Clinic</span></div>
  <div class="person">Dr. Kelsi Tomberg Ravinder</div>
  <div class="contact tiny">Phone: 02 5173 6648<br>Mobile: 04 7825 1943<br>kelsi@HarbourleaDentalClinic.com.au<br>www.HarbourleaDentalClinic.com.au</div>
  <svg class="wave" viewBox="0 0 209 10" height="10" preserveAspectRatio="none"><path d="M0 5 C70 0 140 10 209 2 V10 H0Z" fill="var(--blue)"/></svg>
</div>
<div class="sheet email-card">
  <div class="brand"><span class="brand-dot"></span><span class="brand-name">Harbourlea Dental Clinic</span></div>
  <div class="contact tiny">Appointment: For - Date - Time<br>Please contact us if you cannot attend.</div>
</div>

</body>
</html>
```